Create a Magazine Ad for an asbestos law firm

we need an 8 X 13 ad to be on the back of a magazine cover. We have the text Attached and want a similar look and feel to our website : www.harborvale-claims.example. The ad should be targeted to white males 55 years or older who are conservative and worked in industry or industrial plants. The main offer is a free case review and trying to get them to call the telephone number.

Target Market(s)

White collar men who worked in industrial plants. Age 55 years or older.

Industry/Entity Type

Legal

Requirements
Must have
• Pictures of white middle class conservative man or man and woman
Nice to have
• look at www.harborvale-claims.example to an. idea of what we are looking for

```html
<!DOCTYPE html>
<html lang="en">
<head>
<meta charset="utf-8">
<title>Carrow &amp; Whitfield – Mesothelioma Magazine Ad</title>
<link href="https://fonts.googleapis.com/css2?family=Montserrat:wght@400;500;600;700;800&display=swap" rel="stylesheet">
<style>
  :root {
    --ink: #2a2d34;
    --ink-soft: #333740;
    --gold: #fcc133;
    --paper: #f3f4f5;
    --white: #ffffff;
    --canvas: #dedede;
    --rule: #c9cbd0;
  }
  * { margin: 0; padding: 0; box-sizing: border-box; }
  html, body { width: 1200px; height: 1200px; overflow: hidden; background: var(--canvas); }
  body { font-family: "Montserrat", Arial, sans-serif; position: relative; }

  .ad {
    position: absolute; left: 249px; top: 30px;
    width: 1040px; height: 1690px;
    transform: scale(0.6746); transform-origin: top left;
    background: var(--paper); overflow: hidden;
  }
  .abs { position: absolute; }

  /* hero */
  .hero { left: 0; top: 0; width: 1040px; height: 525px;
    background: radial-gradient(ellipse at 55% 10%, #4a4d48 0%, #2e3033 45%, var(--ink) 80%); }
  .hero-photo { left: 515px; top: 0; width: 525px; height: 525px;
    background: linear-gradient(200deg, #3c4034 0%, #6f7a8c 40%, #c9a98c 75%, #e8d3bd 100%); }
  .brand { left: 45px; top: 68px; display: flex; align-items: center; gap: 14px;
    color: var(--white); font-weight: 600; font-size: 22px; letter-spacing: .04em; }
  .brand-mark { width: 44px; height: 44px; background: var(--white); }
  .hero-title { left: 48px; top: 158px; color: var(--gold); font-weight: 700; font-size: 28px; line-height: 35px; }
  .hero-lead { left: 47px; top: 256px; width: 450px; color: var(--white); font-weight: 600; font-size: 19.5px; line-height: 24px; }
  .ticks { list-style: none; }
  .ticks li { display: flex; align-items: center; gap: 10px; font-size: 19.5px; height: 31px; }
  .ticks svg { width: 17px; height: 17px; flex: none; }
  .hero-ticks { left: 46px; top: 383px; color: var(--white); font-weight: 600; }

  .gold-rule { left: 0; width: 1040px; height: 10px; background: var(--gold); }

  /* info */
  .pill { left: 46px; height: 42px; border-radius: 21px; display: flex; align-items: center; padding-left: 28px; font-weight: 700; }
  .pill-dark { top: 562px; width: 720px; background: var(--ink); color: var(--gold); font-size: 20px; }
  .pill-gold { background: var(--gold); color: var(--ink); font-size: 24px; }
  .info-ticks { left: 46px; top: 619px; color: var(--ink); font-weight: 600; }
  .body-copy { left: 46px; width: 950px; color: var(--ink-soft); font-size: 19.5px; line-height: 24px; }

  /* results */
  .results { left: 0; top: 1083px; width: 1040px; height: 342px; background: var(--ink); }
  .result { position: absolute; color: var(--white); font-size: 21px; }
  .result b { display: block; color: var(--gold); font-size: 26px; font-weight: 700; margin-bottom: 8px; }
  .h-rule { position: absolute; left: 47px; width: 946px; height: 2px; background: var(--rule); }
  .v-rule { position: absolute; left: 509px; top: 39px; width: 2px; height: 268px; background: var(--rule); }

  /* call to action */
  .cta-band { left: 0; top: 1437px; width: 1040px; height: 115px; background: var(--gold); }
  .cta-copy { left: 40px; top: 1462px; width: 960px; text-align: center; color: var(--ink); font-size: 21px; line-height: 26px; }
  .cta-copy strong { font-weight: 700; }
  .footer { left: 0; top: 1552px; width: 1040px; height: 138px; background: var(--ink); }
  .cta-button { left: 292px; top: 1532px; width: 456px; height: 40px; border-radius: 20px; background: var(--white);
    color: var(--ink); font-size: 25px; font-weight: 500; display: flex; align-items: center; justify-content: center; }
  .phone { left: 0; top: 1576px; width: 1040px; text-align: center; color: var(--gold); font-size: 50px; font-weight: 800; letter-spacing: .01em; }
  .firm-line { left: 0; top: 1634px; width: 1040px; text-align: center; color: var(--white); font-size: 19.5px; font-weight: 600; }
</style>
</head>
<body>
<svg width="0" height="0" style="position:absolute">
  <defs>
    <symbol id="tick" viewBox="0 0 20 20">
      <circle cx="9" cy="11" r="7" fill="none" stroke="currentColor" stroke-width="2"/>
      <path d="M5 11 l4 4 L19 3" fill="none" stroke="currentColor" stroke-width="2.6" stroke-linecap="round" stroke-linejoin="round"/>
    </symbol>
  </defs>
</svg>

<article class="ad">
  <section class="hero abs"></section>
  <div class="hero-photo abs" role="img" aria-label="Photo of a smiling senior couple embracing outdoors"></div>

  <div class="brand abs"><span class="brand-mark"></span>Carrow &amp; Whitfield, LLP</div>

  <h1 class="hero-title abs">Diagnosed with Mesothelioma,<br>You could be Owed Compensation</h1>
  <p class="hero-lead abs">It's very likely you developed this disease through asbestos exposure. Mesothelioma patients are getting multi-million dollar settlements, decades later, from:</p>
  <ul class="ticks hero-ticks abs">
    <li><svg style="color:var(--gold)"><use href="#tick"/></svg>Exposure to asbestos products,</li>
    <li><svg style="color:var(--gold)"><use href="#tick"/></svg>Ex-employers, or</li>
    <li><svg style="color:var(--gold)"><use href="#tick"/></svg>Talcum baby powder companies.</li>
  </ul>

  <div class="gold-rule abs" style="top:525px"></div>

  <div class="pill pill-dark abs">We can help you find out if you qualify for a case in minutes.</div>
  <ul class="ticks info-ticks abs">
    <li><svg style="color:var(--ink)"><use href="#tick"/></svg>We'll analyze your situation at no cost</li>
    <li><svg style="color:var(--ink)"><use href="#tick"/></svg>Determine how much compensation you could be entitled too</li>
    <li><svg style="color:var(--ink)"><use href="#tick"/></svg>Show you the next steps to get what you're owed</li>
  </ul>

  <h2 class="pill pill-gold abs" style="top:733px;width:793px">$30 Billion is Available in Trust for Mesothelioma Patients</h2>
  <p class="body-copy abs" style="top:793px">Tradesmen in many industries were negligently exposed to asbestos materials well into the 1990s. Whether you developed Mesothelioma yourself due to asbestos exposure or you're the surviving family of a lost loved one you could be entitled to significant compensation.</p>

  <h2 class="pill pill-gold abs" style="top:892px;width:912px">How much Money Can People Receive from a Mesothelioma Case?</h2>
  <p class="body-copy abs" style="top:951px">Depending on where you were exposed and a few other factors, you can get a settlement from 6 to 7 figures. Here are a few examples of Mesothelioma Settlements received by our clients. These figures are the total compensation after all attorney fees and expenses are deducted.</p>

  <div class="gold-rule abs" style="top:1073px"></div>

  <section class="results abs">
    <div class="result" style="left:48px;top:28px"><b>$6,142,500</b>Exposed through heavy duty vehicles</div>
    <div class="result" style="left:554px;top:31px"><b>$3,921,750</b>Exposed through navy service</div>
    <div class="h-rule" style="top:110px"></div>
    <div class="result" style="left:48px;top:131px"><b>$6,033,510</b>Exposed through general contracting</div>
    <div class="result" style="left:554px;top:134px"><b>$3,600,450</b>Exposed through navy service</div>
    <div class="h-rule" style="top:213px"></div>
    <div class="result" style="left:48px;top:234px"><b>$5,939,010</b>Exposed through boat repair</div>
    <div class="result" style="left:554px;top:237px"><b>$2.5 Million</b>Exposed from Brightfield Talcum Baby Powder.</div>
    <div class="v-rule"></div>
  </section>

  <div class="cta-band abs"></div>
  <p class="cta-copy abs"><strong>Find out if you're Eligible, for FREE, in Minutes.</strong> We'll evaluate your situation and tell you what your case could be worth.</p>
  <footer class="footer abs"></footer>
  <div class="cta-button abs">Get your Free evaluation now!</div>
  <p class="phone abs">1-855-555-0148</p>
  <p class="firm-line abs">Carrow &amp; Whitfield, LLP, Daniel Carrow, Riverton, TX</p>
</article>
</body>
</html>
```